Criação de Kit com 6 Layouts de Post para Redes Sociais (Facebook, Instagram e etc) para Saúde & Nutrição
" Consultório oftalmológico com ênfase em consultas oftalmológicas, exames complementares e cirurgias oculares "

```html
<!DOCTYPE html>
<html lang="pt-BR">
<head>
<meta charset="UTF-8">
<title>Olhos secos, o que significam?</title>
<link href="https://fonts.googleapis.com/css2?family=Montserrat:wght@400;500;600;700;800&display=swap" rel="stylesheet">
<style>
  :root {
    --navy: #1d2b4c;
    --navy-soft: #2a3a5e;
    --beige: #f2e1b8;
    --beige-deep: #e9d29d;
    --gold: #c7a264;
    --white: #ffffff;
    --text: #2a2f3a;
  }
  * { box-sizing: border-box; margin: 0; padding: 0; }
  html, body { width: 1200px; height: 1200px; overflow: hidden; background: var(--white); }
  .post {
    position: relative;
    width: 1200px;
    height: 1200px;
    overflow: hidden;
    font-family: "Montserrat", sans-serif;
  }
  .scene-photo {
    position: absolute;
    inset: 0;
    background:
      radial-gradient(ellipse 420px 620px at 900px 420px, rgba(120,105,95,0.35), transparent 70%),
      linear-gradient(180deg, rgba(255,255,255,0) 70%, rgba(190,188,184,0.55) 100%),
      linear-gradient(90deg, #f7f6f4 0%, #eeedea 40%, #d8d4cf 75%, #cfcac4 100%);
  }
  .decor {
    position: absolute;
    inset: 0;
    width: 1200px;
    height: 1200px;
  }
  .brand {
    position: absolute;
    left: 168px;
    top: 220px;
    width: 480px;
    color: var(--navy);
    font-weight: 600;
  }
  .brand-mark {
    display: block;
    width: 70px;
    height: 70px;
    border-radius: 50%;
    background: var(--gold);
    margin: 0 0 30px 150px;
  }
  .brand-name {
    font-size: 42px;
    letter-spacing: 1px;
    line-height: 1.1;
    text-transform: uppercase;
  }
  .brand-role {
    margin-top: 14px;
    font-size: 22px;
    letter-spacing: 9px;
    text-transform: uppercase;
    padding-left: 60px;
  }
  .info-card {
    position: absolute;
    left: 336px;
    top: 480px;
    width: 528px;
    height: 336px;
    background: var(--white);
    border-radius: 26px;
    text-align: center;
    padding-top: 34px;
    box-shadow: 0 10px 30px rgba(0,0,0,0.06);
  }
  .info-title {
    color: var(--navy);
    font-weight: 700;
    font-size: 40px;
    line-height: 1.18;
  }
  .info-list {
    list-style: none;
    margin-top: 26px;
    color: var(--text);
    font-size: 21px;
    font-weight: 500;
  }
  .info-list li { margin-bottom: 24px; }
  .cta {
    position: absolute;
    left: 486px;
    top: 784px;
    width: 228px;
    height: 50px;
    border-radius: 25px;
    background: var(--navy);
    color: var(--white);
    font-size: 20px;
    font-weight: 500;
    display: flex;
    align-items: center;
    justify-content: center;
    gap: 12px;
  }
  .cta svg { width: 26px; height: 26px; }
</style>
</head>
<body>
  <main class="post">
    <div class="scene-photo" role="img" aria-label="Foto de uma mulher de óculos em frente ao notebook, cansada, segurando a ponte do nariz com os olhos fechados"></div>

    <svg class="decor" viewBox="0 0 1200 1200" aria-hidden="true">
      <path d="M120 0 A330 330 0 0 0 0 240 L0 140 A240 240 0 0 1 40 0 Z" fill="var(--beige)"/>
      <path d="M0 0 L40 0 A240 240 0 0 0 0 140 Z" fill="var(--white)" opacity="0.7"/>
      <path d="M0 520 C150 520 250 640 250 800 C250 960 150 1080 0 1090 Z" fill="var(--beige)"/>
      <path d="M0 1090 C170 1090 280 1140 300 1200 L0 1200 Z" fill="var(--beige-deep)" opacity="0.6"/>
      <path d="M1200 0 L1200 0" fill="none"/>
    </svg>

    <div class="brand">
      <span class="brand-mark"></span>
      <div class="brand-name">Dra. Helena Varnieri</div>
      <div class="brand-role">Oftalmologista</div>
    </div>

    <section class="info-card">
      <h1 class="info-title">Olhos secos,<br>o que significam?</h1>
      <ul class="info-list">
        <li>Deficiência aquosa no filme lacrimal</li>
        <li>Evaporação excessiva do filme lacrimal</li>
        <li>Disfunção das glândulas de Meibomius</li>
      </ul>
    </section>

    <div class="cta">
      <svg viewBox="0 0 26 26" aria-hidden="true">
        <circle cx="13" cy="13" r="12" fill="var(--white)"/>
        <path d="M11 8 L16 13 L11 18" fill="none" stroke="var(--navy)" stroke-width="2.6" stroke-linecap="round" stroke-linejoin="round"/>
      </svg>
      Fale conosco
    </div>
  </main>
</body>
</html>
```